Creation of a Facebook cover graphic

We need a Facebook cover graphic for a page that will be used to test the market for an online training product.

The Product

The subject of the training is the basic online marketing. The training will be delivered online rather than at a venue.

The name of the website is www.tallowfinchhub.com. PLEASE NOTE We have owned the site domain for a while and the current content is 'NOT' representative of the new product. If Quillbarrow deliver on this project we will be back for the website and logo designs! please note we have included a draft logo concept file attachment with the brief.

Design Details

The cover graphic will be viewed on desktop, tablet and mobile. We have tried to give you a brief that guarantees the profile looks good and is readable on mobile. The design is bold and simple in order to enhance viewing the graphic on mobile.

We have included a draft graphic (Both as psd and png). This only shows layout and content. The draft graphic is mainly text based.

We have also included a concept file for the logo. You may want to incorporate the target and arrow icon contained in that file into the design.

Creating a design optimised for mobile is perhaps more challenging than larger formats. Feel free to designs with the following elements: Backgrounds; shapes; gradients and font/text effects - however try and retain a flat and simple design

Graphic size: 828px x 315px – we prefer this size rather than the mobile specific size. It actually renders best across all devices.
Place the design in between 174px & 650px horizontally as this gives best viewing on mobile. Backgrounds can extend across the whole graphic.
Web resolution

There are 2 section to the design:

Section 1. Title ‘The Bright Harbour Crew’
Section 2. Sub title ’Solving online marketing needs’ and to do listing

For the logo colouring and background we would prefer:

Background colour: #236d99 will be our main corporate colour. Other colours are #00456e, #236d99 and # 82bcd0.
Text colour : white or white with a shade of blue. You may contrast text colour of section 1 and section 2.

Fonts : We have two font styles in the draft (Arial Black and Arial Nova). The mobile first design requires the fonts to be very simple so as the text can be read on mobile devices. You can try similar such as Helvetica, Lato etc.
Icons etc : There are 3 ticks against each element of the to do list. Feel free to creative how you want to work with these.

Examples

The Quillbarrow graphic included in the files is a good example of simplicity and flat design.

Target Market(s)

Our clients will be business owners and managers. Generally, one person, small and medium sized businesses.
Gender : Both male and female.
Typical ages : 35-65
They favour simplicity, functionality and boldness - rather than elegance or sophistication

Industry/Entity Type

Marketing

Font styles to use
Sans Serif

Requirements
Must have
• View well on mobile devices
• Text readable on mobile devices
• Simplicity
• Flatter type of design
Nice to have
• Not really a design idea. Would like some feedback on whether our design brief was useful for you as designers.
Should not have
• Complex and finely detailed design

```html
<!DOCTYPE html>
<html lang="en">
<head>
<meta charset="utf-8">
<title>The Bright Harbour Crew – Cover</title>
<link rel="stylesheet" href="https://fonts.googleapis.com/css2?family=Barlow+Condensed:wght@500;600&display=swap">
<style>
  :root {
    --cover-blue: #2177c6;
    --frame-grey: #4a4f57;
    --title-white: #ffffff;
    --list-aqua: #86dbe3;
    --tick-shadow: #123c7a;
  }
  * { margin: 0; padding: 0; box-sizing: border-box; }
  html, body {
    width: 1200px;
    height: 458px;
    overflow: hidden;
    background: #ffffff;
  }
  .cover {
    position: relative;
    width: 1200px;
    height: 458px;
    background: var(--cover-blue);
    border: 2px solid var(--frame-grey);
    font-family: "Barlow Condensed", "Arial Narrow", sans-serif;
  }
  .cover-title {
    position: absolute;
    top: 74px;
    left: 0;
    width: 100%;
    text-align: center;
    color: var(--title-white);
    font-weight: 600;
    font-size: 62px;
    line-height: 1;
    letter-spacing: 0.5px;
  }
  .cover-subtitle {
    position: absolute;
    top: 140px;
    left: 0;
    width: 100%;
    text-align: center;
    color: var(--title-white);
    font-weight: 600;
    font-size: 34px;
    line-height: 1;
    letter-spacing: 0.3px;
  }
  .needs-list {
    position: absolute;
    top: 230px;
    left: 340px;
    list-style: none;
  }
  .needs-item {
    display: flex;
    align-items: center;
    height: 60px;
    color: var(--list-aqua);
    font-weight: 500;
    font-size: 39px;
    letter-spacing: 0.4px;
  }
  .needs-tick {
    width: 44px;
    height: 40px;
    margin-right: 40px;
    flex: none;
  }
</style>
</head>
<body>
  <main class="cover">
    <h1 class="cover-title">The Bright Harbour Crew</h1>
    <p class="cover-subtitle">Solving Online Marketing Needs</p>
    <ul class="needs-list">
      <li class="needs-item">
        <svg class="needs-tick" viewBox="0 0 44 40" aria-hidden="true">
          <path d="M4 22 L13 20 L19 30 Q28 12 42 3 Q30 16 21 38 Z" fill="var(--tick-shadow)" transform="translate(2 2)"/>
          <path d="M4 22 L13 20 L19 30 Q28 12 42 3 Q30 16 21 38 Z" fill="#ffffff"/>
        </svg>
        Making websites ‘sticky’
      </li>
      <li class="needs-item">
        <svg class="needs-tick" viewBox="0 0 44 40" aria-hidden="true">
          <path d="M4 22 L13 20 L19 30 Q28 12 42 3 Q30 16 21 38 Z" fill="var(--tick-shadow)" transform="translate(2 2)"/>
          <path d="M4 22 L13 20 L19 30 Q28 12 42 3 Q30 16 21 38 Z" fill="#ffffff"/>
        </svg>
        Increasing conversions
      </li>
      <li class="needs-item">
        <svg class="needs-tick" viewBox="0 0 44 40" aria-hidden="true">
          <path d="M4 22 L13 20 L19 30 Q28 12 42 3 Q30 16 21 38 Z" fill="var(--tick-shadow)" transform="translate(2 2)"/>
          <path d="M4 22 L13 20 L19 30 Q28 12 42 3 Q30 16 21 38 Z" fill="#ffffff"/>
        </svg>
        Boosting quality traffic
      </li>
    </ul>
  </main>
</body>
</html>
```